Your Health, Your Time, Your Way: Personalized, Concierge Care Elevated to Modern Medicine

We need to incorporate an image of our new doctor (Dr. Marlene Quorvath, MD) with our office logo ( Bright Harbor Clinic) and dialogue that shows how simple it is to schedule a free consult and learn what our office has to offer patients. The colors should be consistent with our website- the CMYK codes will be attached for your use below. The font should be easy to read. The text should be clear, and convey value to the patient for chosing us over anyone else ( we offer primary care, preventive medicine, urgen care and functional medicine with 24 hour direct access to care with some of our strengths including focus on individualized care, cutting edge medicine, blended functional and traditional style. We aim to transform lives through patient centered innovative and individualized care plan. I have attached a "mock" image but the details ( office address, name, phone number are incorrect) The correct info is Bright Harbor Clinic 4187 Pellman Ave Suite 214, Clearwater, FL 33798 and phone number (727)555-0148. A possible hook could read: welcoming new patients now- Your Health, Your Time, Your Way: Personalized Care Meets Modern Medicine
Updates

I did not realize that there was a tab with more information to fill for the designers to see, or for me to upload the basic information they need to create the design.

Target Market(s)

Patients over 18 years of age with interest in longevity, functional and traditional medicine; the postcards will be mailed to our CURRENT patients, and they are a reminder of what we do, new patient availability AND a request for them to refer friends or families

Industry/Entity Type

medical

Font styles to use
Sans Serif

Colors

Designer to choose colors to be used in the design.

Requirements
Must have
• simple reminder to current patients of what we offer, and a call to action for our patients to refer friends and family for same level of excellence;consistency with brand ( see business card and cmyx codes for colors);photo of new physician; logo Bright Harbor Clinic, web site (https://brightharborclinic.example); Must clearly express accepting new patients; simple to call/email to schedule free consultation;; include our email (frontdesk@brightharborclinic.example), phone number (727)555-0148; our address 4187 Pellman Ave Suite 214, Clearwater, FL 33798
Nice to have
• photo of our new physician ( in blue jacket: Dr. Marlene Quorvath, MD) should not take up too much space
Should not have
• clutter, or close text; full sentences( bulleted text preferred)

```html
<!DOCTYPE html>
<html lang="en">
<head>
<meta charset="utf-8">
<title>Bright Harbor Clinic Postcard</title>
<link href="https://fonts.googleapis.com/css2?family=Gilda+Display&family=Poppins:wght@400;500;600;700&display=swap" rel="stylesheet">
<style>
  :root {
    --slate: #5b6e85;
    --slate-dark: #30353f;
    --paper: #ffffff;
    --mist: #efeeec;
    --rule: #e4e4e4;
    --ink: #2d2f33;
    --stamp: #bcbfc4;
    --backdrop: #d6d6d6;
    --serif: "Gilda Display", Georgia, serif;
    --sans: "Poppins", Arial, sans-serif;
  }
  * { margin: 0; padding: 0; box-sizing: border-box; }
  html, body { width: 1067px; height: 1200px; overflow: hidden; }
  body { background: var(--backdrop); position: relative; font-family: var(--sans); color: var(--ink); }

  .postcard { position: absolute; left: 104px; width: 860px; height: 573px; background: var(--paper); overflow: hidden; box-shadow: 0 2px 8px rgba(0,0,0,.15); }
  .postcard--front { top: 18px; }
  .postcard--back { top: 609px; }
  .postcard svg.shapes { position: absolute; inset: 0; }
  .abs { position: absolute; }

  .brand-name { font-family: var(--serif); color: #111; line-height: 1.05; }
  .front .brand-name { left: 70px; top: 42px; font-size: 34px; }
  .back .brand-name { left: 100px; top: 452px; font-size: 24px; }

  .headline { left: 54px; top: 224px; font-family: var(--serif); color: #fff; font-size: 35px; line-height: 1.05; white-space: nowrap; }
  .subhead { left: 54px; top: 311px; font-family: var(--serif); color: #fff; font-size: 17px; white-space: nowrap; }
  .tagline { left: 53px; top: 357px; font-size: 13.5px; font-weight: 600; color: var(--slate); }
  .intro { left: 55px; top: 380px; width: 750px; text-align: center; font-size: 13.5px; line-height: 16.4px; }
  .intro .referral { font-weight: 600; color: var(--slate); }
  .footer-line { left: 48px; top: 536px; font-size: 12.5px; font-weight: 600; color: #fff; white-space: nowrap; }

  .offer-title { left: 55px; top: 22px; font-family: var(--serif); color: #fff; font-size: 38px; line-height: 1; }
  .offer-list { left: 55px; top: 90px; list-style: none; font-size: 13.5px; line-height: 20.6px; }
  .offer-list li { position: relative; padding-left: 17px; }
  .offer-list li svg { position: absolute; left: 0; top: 5px; }
  .cta { left: 53px; top: 261px; font-size: 17.5px; font-weight: 600; line-height: 21px; color: #fff; }
  .contact-list { left: 55px; top: 329px; list-style: none; font-size: 13.5px; font-weight: 600; line-height: 20.6px; white-space: nowrap; }
  .contact-list li { position: relative; padding-left: 17px; }
  .contact-list li svg { position: absolute; left: 0; top: 5px; }

  .photo { position: absolute; }
  .photo--doctor { left: 292px; top: 358px; width: 196px; height: 215px; border-radius: 96px 96px 0 0; background: linear-gradient(180deg, #3a3a44 0%, #1a1b22 100%); }
  .stamp-box { left: 717px; top: 48px; width: 105px; height: 105px; background: var(--stamp); }
</style>
</head>
<body>

<section class="postcard postcard--front front">
  <svg class="shapes" width="860" height="573" viewBox="0 0 860 573">
    <defs>
      <linearGradient id="teamTone" x1="0" y1="0" x2="1" y2="1">
        <stop offset="0" stop-color="#a7a8b3"/>
        <stop offset="0.5" stop-color="#c9c6c8"/>
        <stop offset="1" stop-color="#b5b5bf"/>
      </linearGradient>
    </defs>
    <polygon points="277,0 860,0 860,349 362,349" fill="url(#teamTone)" role="img" aria-label="Group portrait of the clinic's three smiling physicians in white coats"/>
    <polygon points="0,203 317,203 365,349 0,349" fill="var(--slate)"/>
    <rect x="370" y="353" width="490" height="9" fill="var(--rule)"/>
    <rect x="0" y="516" width="860" height="57" fill="var(--slate-dark)"/>
    <polygon points="784,516 792,516 808,573 800,573" fill="#fff"/>
    <polygon points="796,516 812,516 828,573 812,573" fill="var(--slate)"/>
    <polygon points="816,516 824,516 840,573 832,573" fill="#fff"/>
  </svg>

  <div class="abs brand-name">Bright<br>Harbor<br>Clinic</div>
  <h1 class="abs headline">Welcoming new<br>patients now</h1>
  <p class="abs subhead">Your Health, Your Time, Your Way</p>
  <p class="abs tagline">Personalized Care Meets Modern Medicine</p>
  <p class="abs intro">Concierge Medicine values your goals, time and health. At Bright Harbor Clinic, we focus on individualized care and take insurance algorithms out of the equation. We use cutting edge technology and tests that make sense for you and your health care goals. If you want easy access to your doctor, comfortable one hour or more visits, flexibility of meeting via zoom, on phone or in office, call today 727-555-0148 and speak to Nadia to schedule your free half hour consultation with our doctors. You can meet our friendly and knowledgeable team and see our office space. <span class="referral">Refer your friends and family for the same level of excellence.</span></p>
  <p class="abs footer-line">Bright Harbor Clinic 4187 Pellman Ave Suite 214, Clearwater, FL 33798 and phone number (727)555-0148</p>
</section>

<section class="postcard postcard--back back">
  <svg class="shapes" width="860" height="573" viewBox="0 0 860 573">
    <polygon points="0,11 349,11 418,252 0,252" fill="var(--mist)"/>
    <rect x="0" y="0" width="860" height="11" fill="var(--slate)"/>
    <polygon points="0,0 241,0 257,76 0,76" fill="var(--slate)"/>
    <polygon points="0,252 418,252 436,314 0,314" fill="var(--slate-dark)"/>
  </svg>

  <h2 class="abs offer-title">we offer</h2>
  <ul class="abs offer-list">
    <li><svg width="11" height="11" viewBox="0 0 11 11"><circle cx="5.5" cy="5.5" r="5.5" fill="var(--slate)"/><path d="M3 5.6l1.8 1.8L8 4" stroke="#fff" stroke-width="1.4" fill="none"/></svg>primary care, preventive medicine,</li>
    <li><svg width="11" height="11" viewBox="0 0 11 11"><circle cx="5.5" cy="5.5" r="5.5" fill="var(--slate)"/><path d="M3 5.6l1.8 1.8L8 4" stroke="#fff" stroke-width="1.4" fill="none"/></svg>urgen care and functional medicine</li>
    <li><svg width="11" height="11" viewBox="0 0 11 11"><circle cx="5.5" cy="5.5" r="5.5" fill="var(--slate)"/><path d="M3 5.6l1.8 1.8L8 4" stroke="#fff" stroke-width="1.4" fill="none"/></svg>24 hour direct access to care with some<br>of our strengths including focus on<br>individualized care,</li>
    <li><svg width="11" height="11" viewBox="0 0 11 11"><circle cx="5.5" cy="5.5" r="5.5" fill="var(--slate)"/><path d="M3 5.6l1.8 1.8L8 4" stroke="#fff" stroke-width="1.4" fill="none"/></svg>cutting edge medicine, blended functional<br>and traditional style</li>
  </ul>

  <p class="abs cta">Simple to call/email to schedule<br>Free consultation</p>

  <ul class="abs contact-list">
    <li><svg width="11" height="11" viewBox="0 0 11 11"><circle cx="5.5" cy="5.5" r="5.5" fill="var(--slate)"/><rect x="2.6" y="3.6" width="5.8" height="3.8" fill="none" stroke="#fff" stroke-width="0.9"/><path d="M2.6 3.6l2.9 2.2 2.9-2.2" stroke="#fff" stroke-width="0.9" fill="none"/></svg>frontdesk@brightharborclinic.example</li>
    <li><svg width="11" height="11" viewBox="0 0 11 11"><circle cx="5.5" cy="5.5" r="5.5" fill="var(--slate)"/><path d="M3.4 2.8c.4-.3.8-.2 1 .2l.5 1c.1.3 0 .5-.2.7l-.3.3c.3.7.8 1.2 1.5 1.5l.3-.3c.2-.2.5-.3.7-.2l1 .5c.4.2.5.6.2 1-.6.8-1.500.8-2.4.3-1.1-.6-2-1.5-2.6-2.6-.5-.9-.5-1.8.3-2.4z" fill="#fff"/></svg>(727)555-0148</li>
    <li><svg width="11" height="11" viewBox="0 0 11 11"><circle cx="5.5" cy="5.5" r="5.5" fill="var(--slate)"/><circle cx="5.5" cy="5.5" r="3" fill="none" stroke="#fff" stroke-width="0.8"/><ellipse cx="5.5" cy="5.5" rx="1.3" ry="3" fill="none" stroke="#fff" stroke-width="0.7"/><path d="M2.5 5.5h6" stroke="#fff" stroke-width="0.7"/></svg>brightharborclinic.example</li>
    <li><svg width="11" height="13" viewBox="0 0 11 13"><path d="M5.5 0C2.5 0 .5 2.2.5 4.8c0 3.3 5 8 5 8s5-4.7 5-8C10.5 2.2 8.5 0 5.5 0z" fill="var(--slate)"/><circle cx="5.5" cy="4.8" r="1.8" fill="#fff"/></svg>4187 Pellman Ave Suite 214,<br>Clearwater, FL 33798</li>
  </ul>

  <div class="abs brand-name">Bright<br>Harbor<br>Clinic</div>
  <div class="photo photo--doctor" role="img" aria-label="Portrait of Dr. Marlene Quorvath, MD, in a dark jacket"></div>
  <div class="abs stamp-box"></div>
</section>

</body>
</html>
```